Business Card Design for Logistics Startup

Link to my logo source file -
https://www.filecrate-demo.net/sh/qx7vmp2lr9kdwta/BBTzY4_LQm8hRuPoKvxVc?dl=0

We want a statement in our business card!
I have go thru your portfolio, and invites 3 of you guys to design my business card as the previous designer cannot give me the feel.
Let me know if you want any information.
Thanks.

Target Market(s)

Transport and Logistics
: Shippers, Freight Forwarders and Carriers.

Industry/Entity Type

Business

Contact Information for Business Card

Our details;

Name: Marcus Lim
Designation: General Manager
Mobile: +65 93415062
Email: marcus.lim@korvanth.com
Address: 7 Jalan Merpati Rise
TRINOX Plaza #03-17
Singapore 612379

Name: Daniel Ho
Designation: Director
Mobile: +65 97264318
Email: daniel.ho@korvanth.com
TRINOX Plaza #03-17
Singapore 612379

Colors
f37122

Requirements
Must have
• Logo from my source file.
• Please included tagline: Transport and Logistics
• If you guy can think of a tagline - Using E and S, that will be perfect. Such as Excellence in Service..

```html
<!DOCTYPE html>
<html lang="en">
<head>
<meta charset="utf-8">
<title>Korvanth Business Card</title>
<link rel="stylesheet" href="https://fonts.googleapis.com/css2?family=Open+Sans:wght@400;600;700&display=swap">
<style>
  :root {
    --stage: #e9e6e2;
    --card-orange: #f17425;
    --ink: #1c1c1c;
    --ink-soft: #2a2320;
  }
  * { margin: 0; padding: 0; box-sizing: border-box; }
  html, body { width: 1200px; height: 1000px; overflow: hidden; }
  body {
    background: var(--stage);
    font-family: "Open Sans", Arial, sans-serif;
    color: var(--ink);
    position: relative;
  }
  .card {
    position: absolute;
    left: 266px;
    width: 666px;
    height: 397px;
    border-radius: 22px;
    background: var(--card-orange);
  }
  .card--front { top: 74px; }
  .card--back { top: 533px; }

  /* Front: brand block */
  .front-brand {
    position: absolute;
    left: 40px;
    top: 110px;
    width: 290px;
    text-align: center;
  }
  .front-brand__row {
    display: flex;
    align-items: center;
    justify-content: center;
    gap: 12px;
  }
  .brand-dot {
    width: 14px; height: 14px;
    border-radius: 50%;
    background: var(--ink);
  }
  .front-brand__name {
    font-size: 34px;
    font-weight: 600;
    letter-spacing: 4px;
    color: var(--ink);
  }
  .front-brand__sector {
    margin-top: 14px;
    font-size: 14px;
    letter-spacing: 3px;
    text-transform: uppercase;
    color: var(--ink-soft);
  }

  /* Front: contact block */
  .contact {
    position: absolute;
    left: 375px;
    top: 82px;
  }
  .contact__name {
    font-size: 21px;
    font-weight: 700;
    line-height: 26px;
    text-transform: uppercase;
  }
  .contact__role {
    font-size: 16px;
    line-height: 24px;
  }
  .contact__address {
    margin-top: 20px;
    font-size: 16px;
    line-height: 23.5px;
    font-style: normal;
  }
  .contact__lines {
    list-style: none;
    margin-top: 14px;
    font-size: 16px;
    line-height: 24.5px;
  }
  .contact__lines li { display: flex; align-items: center; gap: 6px; }
  .contact__icon { width: 15px; height: 13px; flex: none; }

  /* Back */
  .back-brand__mark {
    position: absolute;
    left: 91px;
    top: 160px;
    width: 60px; height: 60px;
    background: var(--ink);
  }
  .back-brand__name {
    position: absolute;
    left: 249px;
    top: 160px;
    line-height: 60px;
    font-size: 36px;
    font-weight: 600;
    letter-spacing: 4px;
    color: var(--ink);
  }
  .back-tagline {
    position: absolute;
    left: 0; right: 0;
    top: 346px;
    text-align: center;
    font-size: 16px;
    letter-spacing: 1.6px;
    color: var(--ink);
  }
</style>
</head>
<body>

<section class="card card--front" aria-label="Business card front">
  <div class="front-brand">
    <div class="front-brand__row">
      <span class="brand-dot" aria-hidden="true"></span>
      <span class="front-brand__name">KORVANTH</span>
    </div>
    <p class="front-brand__sector">Transport &amp; Logistics</p>
  </div>

  <div class="contact">
    <h1 class="contact__name">Marcus Lim</h1>
    <p class="contact__role">General Manager</p>
    <address class="contact__address">
      7 Jalan Merpati Rise<br>
      TRINOX Plaza #03-17<br>
      Singapore 612379
    </address>
    <ul class="contact__lines">
      <li>
        <svg class="contact__icon" viewBox="0 0 15 13" aria-hidden="true">
          <path d="M1 4 Q7.5 0 14 4 L12.5 6 L10 4.8 L10 3.6 Q7.5 2.8 5 3.6 L5 4.8 L2.5 6 Z" fill="#1c1c1c"/>
          <rect x="3" y="7" width="9" height="5" rx="1" fill="#1c1c1c"/>
        </svg>
        <span>+65 93415062</span>
      </li>
      <li>
        <svg class="contact__icon" viewBox="0 0 15 13" aria-hidden="true">
          <rect x="1" y="2" width="13" height="9" fill="#1c1c1c"/>
          <path d="M1.5 2.5 L7.5 7 L13.5 2.5" stroke="#f17425" stroke-width="1.2" fill="none"/>
        </svg>
        <span>marcus.lim@korvanth.com</span>
      </li>
      <li>
        <svg class="contact__icon" viewBox="0 0 15 13" aria-hidden="true">
          <circle cx="7.5" cy="6.5" r="5.8" fill="#1c1c1c"/>
          <path d="M1.7 6.5 H13.3 M7.5 0.7 V12.3" stroke="#f17425" stroke-width="0.9"/>
          <ellipse cx="7.5" cy="6.5" rx="2.6" ry="5.8" fill="none" stroke="#f17425" stroke-width="0.9"/>
        </svg>
        <span>www.korvanth-freight.com</span>
      </li>
    </ul>
  </div>
</section>

<section class="card card--back" aria-label="Business card back">
  <span class="back-brand__mark" aria-hidden="true"></span>
  <span class="back-brand__name">KORVANTH</span>
  <p class="back-tagline">Every Load Counts | We Carry It With Care</p>
</section>

</body>
</html>
```